Business Card for Industrial Distributor

We need a business card design for an industrial distributor. We sell machine parts for the manufacturing and oil industry. We would like the cards to look clean and modern but with a touch of industry.

Our colors are blue/white.

Please feel free to visit our website www.krovelmint.com

Target Market(s)

mexican manufacturers in the automobile/aerospace industry

Industry/Entity Type

Industrial

Colors
ffffff
0555a3

```html
<!DOCTYPE html>
<html lang="en">
<head>
<meta charset="utf-8">
<title>Krovelmint Business Card</title>
<link href="https://fonts.googleapis.com/css2?family=Arimo:wght@400;700&display=swap" rel="stylesheet">
<style>
  :root {
    --backdrop: #3b3431;
    --card: #161618;
    --card-edge: #0d0d0e;
    --silver: #b9bcc0;
    --muted: #8b8e93;
    --white: #f2f2f2;
    --brand-blue: #2f56c8;
    --brand-blue-deep: #0555a3;
    --divider: #9a9a9a;
  }
  * { margin: 0; padding: 0; box-sizing: border-box; }
  html, body {
    width: 1200px; height: 864px; overflow: hidden;
    background: var(--backdrop);
    font-family: "Arimo", Arial, sans-serif;
  }
  .canvas {
    position: relative; width: 1200px; height: 864px;
  }
  .card {
    position: absolute; left: 300px;
    width: 600px; height: 343px;
    background: var(--card);
    border-radius: 4px;
    box-shadow: 0 10px 24px rgba(0,0,0,.45);
    overflow: hidden;
  }
  .card--front { top: 70px; }
  .card--back { top: 451px; }

  /* Front */
  .front-brand {
    position: absolute; left: 0; right: 0; top: 110px;
    display: flex; align-items: center; justify-content: center; gap: 18px;
  }
  .front-brand__dot {
    width: 58px; height: 58px; border-radius: 50%;
    background: var(--silver);
  }
  .front-brand__name {
    font-size: 64px; font-weight: 700; color: var(--silver);
    letter-spacing: 1px;
  }
  .front-url {
    position: absolute; left: 0; right: 0; top: 222px;
    text-align: center; font-size: 14px; letter-spacing: 6px;
    color: var(--muted);
  }

  /* Back */
  .back-mark {
    position: absolute; left: 56px; top: 66px; width: 210px;
    display: flex; flex-direction: column; align-items: center; gap: 14px;
  }
  .back-mark__circle {
    width: 170px; height: 170px; border-radius: 50%;
    background: var(--brand-blue);
  }
  .back-mark__name {
    font-size: 26px; font-weight: 700; color: var(--white);
  }
  .back-divider {
    position: absolute; left: 300px; top: 46px;
    width: 1px; height: 250px; background: var(--divider);
  }
  .contact {
    position: absolute; left: 326px; top: 62px; color: var(--white);
  }
  .contact__name {
    font-size: 20px; color: var(--brand-blue); letter-spacing: .5px;
  }
  .contact__role { font-size: 17px; margin-top: 2px; }
  .contact__address {
    font-size: 14px; line-height: 1.3; margin-top: 16px; color: #dcdcdc;
  }
  .contact__list { list-style: none; margin-top: 14px; }
  .contact__item {
    display: flex; align-items: center; gap: 10px;
    font-size: 16px; line-height: 1.5;
  }
  .contact__icon { width: 15px; height: 15px; fill: var(--brand-blue); flex: none; }
  .contact__item--plain { padding-left: 0; }
</style>
</head>
<body>
<main class="canvas">

  <section class="card card--front" aria-label="Card front">
    <div class="front-brand">
      <span class="front-brand__dot"></span>
      <span class="front-brand__name">Krovelmint</span>
    </div>
    <p class="front-url">www.krovelmint.com</p>
  </section>

  <section class="card card--back" aria-label="Card back">
    <div class="back-mark">
      <span class="back-mark__circle"></span>
      <span class="back-mark__name">Krovelmint</span>
    </div>
    <div class="back-divider"></div>
    <div class="contact">
      <p class="contact__name">MARCUS HALE</p>
      <p class="contact__role">President</p>
      <p class="contact__address">Krovelmint International Corp.<br>4820 Alder Ridge Rd.<br>Harlow,TX 78990</p>
      <ul class="contact__list">
        <li class="contact__item">
          <svg class="contact__icon" viewBox="0 0 16 16" aria-hidden="true"><path d="M2 5c0-2 2-3 6-3s6 1 6 3v1h-3V4.5H5V6H2z"/><rect x="3" y="7" width="10" height="7" rx="1.5"/></svg>
          (555) 318 - 4402
        </li>
        <li class="contact__item">
          <svg class="contact__icon" viewBox="0 0 16 16" aria-hidden="true"><rect x="4" y="1" width="8" height="5"/><rect x="1" y="6" width="14" height="6" rx="1"/><rect x="4" y="10" width="8" height="5"/></svg>
          (555) 318 - 4417
        </li>
        <li class="contact__item">
          <svg class="contact__icon" viewBox="0 0 16 16" aria-hidden="true"><path d="M1 3h14v10H1z M2 4l6 5 6-5" stroke="#161618" stroke-width="1"/></svg>
          sales@krovelmint.com
        </li>
        <li class="contact__item">
          <svg class="contact__icon" viewBox="0 0 16 16" aria-hidden="true"><circle cx="8" cy="8" r="7"/><path d="M1 8h14M8 1c-3 3-3 11 0 14M8 1c3 3 3 11 0 14" stroke="#161618" stroke-width="1" fill="none"/></svg>
          www.krovelmint.com
        </li>
      </ul>
    </div>
  </section>

</main>
</body>
</html>
```